Old-fashioned Candy Label Design (4 different candies)

Four new labels: Wee Pebbles, Plumberry Slab, Wattlebark Pips, Kestrel Rings (Peppermint), each 105x45mm finished size, need to supply high-resolution .ai, .eps, and .jpg, files of all labels, including separate images of background, text and any other aspect of the label.

Brand: Marlow Bros. I have no current logo so you are welcome to include a logo design or interesting font that could be used as the logo

Details and accuracy very important!

I will supply all data needed for ingredients, nutritional label and unique barcode after I select a designer. For your mock ups, just put in something like the top one to fill the space the correct information will fill.

Ideas:
• Old fashioned design
• Wee Pebbles – randomly placed multi-coloured polka dots on a white background
• Plumberry Slab – pink/green stripes
• Wattlebark Pips – little gum leaves
• Kestrel Rings – red/white stripes

Please see attached brief for these and additional details.

Thanks!

Font styles to use
Other font styles liked:
• TBA

Requirements
Must have
• old-fashioned look

```html
<!DOCTYPE html>
<html lang="en">
<head>
<meta charset="utf-8">
<title>Marlow Bros. Candy Labels</title>
<link rel="stylesheet" href="https://fonts.googleapis.com/css2?family=Yellowtail&family=Bebas+Neue&family=Josefin+Sans:wght@600&family=Old+Standard+TT&family=Montserrat:wght@700&display=swap">
<style>
  :root {
    --paper: #ffffff;
    --pink: #f57fa5;
    --cream: #f5e6d0;
    --green: #5fc98a;
    --leaf-bg: #d5e9d6;
    --leaf: #8cc99a;
    --red: #f07068;
    --grey: #555555;
    --shadow: #cfcfcf;
  }
  html, body {
    margin: 0;
    width: 1200px;
    height: 1200px;
    overflow: hidden;
    background: var(--paper);
  }
  .label-sheet {
    position: absolute;
    left: 40px;
    top: 348px;
    display: grid;
    grid-template-columns: 540px 540px;
    grid-template-rows: 232px 232px;
    gap: 40px;
  }
  .candy-label {
    width: 540px;
    height: 232px;
    display: block;
    box-shadow: 0 2px 8px rgba(0,0,0,0.12);
  }
  .brand {
    font-family: "Josefin Sans", sans-serif;
    font-weight: 600;
    font-size: 20px;
    letter-spacing: 3px;
  }
  .name-block { font-family: "Bebas Neue", sans-serif; }
  .name-script { font-family: "Yellowtail", cursive; }
  .name-sans { font-family: "Josefin Sans", sans-serif; font-weight: 600; }
  .name-serif { font-family: "Old Standard TT", serif; }
  .net { font-family: "Montserrat", sans-serif; font-weight: 700; }
</style>
</head>
<body>
<main class="label-sheet">

  <!-- Wee Pebbles -->
  <svg class="candy-label label-pebbles" viewBox="0 0 540 232">
    <defs>
      <linearGradient id="pebbles-tone" x1="0" y1="0" x2="1" y2="1">
        <stop offset="0" stop-color="#fdf3f7"/>
        <stop offset="0.5" stop-color="#ffffff"/>
        <stop offset="1" stop-color="#f1f8fc"/>
      </linearGradient>
    </defs>
    <rect width="540" height="232" fill="url(#pebbles-tone)" role="img" aria-label="Randomly placed multi-coloured polka dots on white"/>
    <rect x="68" y="38" width="404" height="140" rx="44" fill="var(--paper)" stroke="var(--pink)" stroke-width="4"/>
    <rect x="80" y="48" width="380" height="120" rx="36" fill="none" stroke="var(--pink)" stroke-width="1.5"/>
    <text class="brand" x="270" y="84" text-anchor="middle" fill="var(--pink)">MARLOW BROS.</text>
    <text class="name-block" x="273" y="151" text-anchor="middle" font-size="64" fill="var(--shadow)">WEE PEBBLES</text>
    <text class="name-block" x="270" y="148" text-anchor="middle" font-size="64" fill="var(--pink)">WEE PEBBLES</text>
    <text class="net" x="270" y="204" text-anchor="middle" font-size="14" fill="var(--pink)">170G</text>
    <text class="net" x="270" y="218" text-anchor="middle" font-size="10" fill="var(--pink)">NET</text>
  </svg>

  <!-- Plumberry Slab -->
  <svg class="candy-label label-plumberry" viewBox="0 0 540 232">
    <defs>
      <pattern id="pink-green-stripes" width="72" height="232" patternUnits="userSpaceOnUse">
        <rect x="0" width="18" height="232" fill="var(--pink)"/>
        <rect x="18" width="18" height="232" fill="var(--cream)"/>
        <rect x="36" width="18" height="232" fill="var(--green)"/>
        <rect x="54" width="18" height="232" fill="var(--cream)"/>
      </pattern>
    </defs>
    <rect width="540" height="232" fill="url(#pink-green-stripes)"/>
    <rect x="18" y="24" width="504" height="166" rx="70" fill="var(--cream)" stroke="var(--green)" stroke-width="4"/>
    <text class="brand" x="270" y="70" text-anchor="middle" fill="var(--pink)">MARLOW BROS.</text>
    <text class="name-script" x="270" y="126" text-anchor="middle" font-size="54" fill="var(--pink)">Plumberry</text>
    <text class="name-block" x="270" y="172" text-anchor="middle" font-size="40" fill="var(--pink)">SLAB</text>
    <rect x="244" y="196" width="52" height="32" fill="var(--cream)"/>
    <text class="net" x="270" y="211" text-anchor="middle" font-size="14" fill="var(--grey)">170G</text>
    <text class="net" x="270" y="224" text-anchor="middle" font-size="10" fill="var(--grey)">NET</text>
  </svg>

  <!-- Wattlebark Pips -->
  <svg class="candy-label label-wattlebark" viewBox="0 0 540 232">
    <rect width="540" height="232" fill="var(--leaf-bg)" role="img" aria-label="Scattered little gum leaves in soft green"/>
    <rect x="68" y="34" width="404" height="150" rx="16" fill="var(--leaf-bg)" stroke="var(--paper)" stroke-width="4"/>
    <rect x="80" y="44" width="380" height="130" rx="10" fill="none" stroke="var(--paper)" stroke-width="1.5"/>
    <text class="brand" x="270" y="78" text-anchor="middle" fill="var(--leaf)">MARLOW BROS.</text>
    <text class="name-sans" x="270" y="126" text-anchor="middle" font-size="40" fill="var(--leaf)">WATTLEBARK</text>
    <text class="name-sans" x="270" y="164" text-anchor="middle" font-size="34" fill="var(--leaf)">PIPS</text>
    <text class="net" x="270" y="206" text-anchor="middle" font-size="14" fill="var(--grey)">170G</text>
    <text class="net" x="270" y="220" text-anchor="middle" font-size="10" fill="var(--grey)">NET</text>
  </svg>

  <!-- Kestrel Rings -->
  <svg class="candy-label label-kestrel-rings" viewBox="0 0 540 232">
    <defs>
      <pattern id="red-white-stripes" width="44" height="232" patternUnits="userSpaceOnUse">
        <rect x="0" width="22" height="232" fill="var(--red)"/>
        <rect x="22" width="22" height="232" fill="var(--paper)"/>
      </pattern>
    </defs>
    <rect width="540" height="232" fill="url(#red-white-stripes)"/>
    <rect x="40" y="30" width="460" height="160" rx="60" fill="var(--red)" stroke="var(--paper)" stroke-width="4"/>
    <text class="brand" x="270" y="72" text-anchor="middle" fill="var(--paper)">MARLOW BROS.</text>
    <text class="name-serif" x="270" y="120" text-anchor="middle" font-size="42" fill="var(--paper)">KESTREL</text>
    <text class="name-serif" x="270" y="166" text-anchor="middle" font-size="42" fill="var(--paper)">RINGS</text>
    <rect x="244" y="196" width="52" height="32" fill="var(--paper)"/>
    <text class="net" x="270" y="211" text-anchor="middle" font-size="14" fill="var(--grey)">170G</text>
    <text class="net" x="270" y="224" text-anchor="middle" font-size="10" fill="var(--grey)">NET</text>
  </svg>

</main>
</body>
</html>
```